Cherish Every Note - Days Ring True

I need a website. I had a company doing it, and it looked very nice, but they went way up on hosting costs and said they owned the design of the site. I changed hosts to keep costs down. You can see the current design at farvalecaudio.example. They said I could use the copy and images from the current website. So you could cut and paste to speed things up. My logo and other images are on the current website. If you are unable to use I can send other digital copies.

Target Market(s)

seniors 55 and up

Number of Pages Required

4 page

Font styles to use
Sans Serif

Colors
0255a3
f78f20

Requirements
Must have
• Video testimonies that I can add without assistance. I use youtube links for the videos.
Nice to have
• The color scheme theme can be drawn from the logo, which is on the current webstie farvalecaudio.example
Should not have
• Should not have anything related to TonVo on the website.

```html
<!DOCTYPE html>
<html lang="en">
<head>
<meta charset="utf-8">
<title>Farvale Hearing Center – Home</title>
<link href="https://fonts.googleapis.com/css2?family=Poppins:ital,wght@0,300;0,400;0,500;0,600;0,700;0,800;1,500&display=swap" rel="stylesheet">
<style>
:root{
  --blue:#0255a3;
  --blue-bar:#1b4f9a;
  --navy:#15385f;
  --orange:#f78f20;
  --orange-band:#f5891a;
  --ink:#2b2f38;
  --grey-title:#5c6577;
  --footer-deep:#171c27;
  --white:#ffffff;
}
*{margin:0;padding:0;box-sizing:border-box}
html,body{width:1200px;height:1200px;overflow:hidden;background:var(--white)}
body{font-family:"Poppins",sans-serif;color:var(--ink)}
.stage{position:absolute;left:0;top:0;width:1932px;height:1932px;transform:scale(.62112);transform-origin:0 0}
.abs{position:absolute}

/* top bar */
.topbar{left:656px;top:0;width:650px;height:17px;background:var(--blue-bar);color:var(--white);font-size:5.5px;font-weight:500}
.topbar span{position:absolute;top:5px;display:flex;align-items:center;gap:4px;white-space:nowrap}
.topbar svg{width:6px;height:6px}

/* header */
.brand{left:745px;top:25px;display:flex;align-items:center;gap:4px}
.brand-mark{width:20px;height:20px;border-radius:50%;background:var(--orange)}
.brand-name{font-size:7px;font-weight:600;color:var(--blue);line-height:8px;letter-spacing:.2px}
.nav{top:33px;font-size:5.6px;font-weight:500;color:var(--ink);letter-spacing:.3px;white-space:nowrap}
.nav.active{color:var(--orange)}

/* hero */
.hero{left:657px;top:55px;width:650px;height:300px;
  background:
    radial-gradient(ellipse 90px 70px at 52% 22%,rgba(214,168,140,.85),transparent 70%),
    radial-gradient(ellipse 120px 90px at 64% 18%,rgba(92,62,44,.9),transparent 75%),
    radial-gradient(ellipse 110px 70px at 72% 42%,rgba(58,70,110,.75),transparent 75%),
    radial-gradient(ellipse 150px 90px at 74% 78%,rgba(214,160,160,.9),transparent 72%),
    radial-gradient(ellipse 160px 70px at 50% 82%,rgba(210,200,190,.85),transparent 72%),
    radial-gradient(ellipse 200px 130px at 15% 75%,rgba(110,108,104,.9),transparent 75%),
    linear-gradient(90deg,#3f3f3f 0%,#6a6562 40%,#7a6f68 65%,#4a4746 100%)}
.hero-shade{left:657px;top:55px;width:650px;height:300px;background:rgba(20,20,24,.28)}
.hero-title{left:657px;width:650px;top:152px;text-align:center;font-size:28.5px;font-weight:800;color:var(--white);letter-spacing:-.3px;line-height:40px}
.hero-title em{font-style:normal;color:var(--orange)}
.hero-sub{left:657px;width:650px;top:190px;text-align:center;font-size:12px;font-weight:300;color:var(--white)}
.btn{background:var(--orange);color:var(--white);font-weight:600;font-size:5.8px;border-radius:3px;display:flex;align-items:center;justify-content:center;letter-spacing:.3px}

/* welcome */
.eyebrow{left:744px;top:400px;font-size:7px;font-weight:700}
.welcome-title{left:743px;top:410px;font-size:15.5px;font-weight:700;color:var(--orange);white-space:nowrap}
.welcome-copy{left:744px;top:438px;width:246px;font-size:5.6px;line-height:12.2px;color:#4a4f5a;letter-spacing:.15px}
.doctor{left:1020px;top:365px;width:202px;height:180px;
  background:
    radial-gradient(ellipse 30px 36px at 55% 20%,#d9a890,transparent 75%),
    radial-gradient(ellipse 10px 40px at 58% 62%,#d8a23a,transparent 80%),
    radial-gradient(ellipse 34px 60px at 56% 62%,#2d4f8f,transparent 80%),
    radial-gradient(ellipse 80px 80px at 55% 78%,#f1f2f4,transparent 80%),
    radial-gradient(ellipse 22px 40px at 12% 45%,#c99b8d,transparent 80%),
    radial-gradient(ellipse 22px 40px at 90% 40%,#c48b80,transparent 80%),
    radial-gradient(ellipse 40px 60px at 90% 70%,#b9c8d8,transparent 80%),
    #f4f5f7;
  -webkit-mask-image:radial-gradient(ellipse 70% 80% at 55% 55%,#000 55%,transparent 100%);
  mask-image:radial-gradient(ellipse 70% 80% at 55% 55%,#000 55%,transparent 100%)}

/* 50 ways */
.ways{left:662px;top:545px;width:640px;height:228px;
  background:
    radial-gradient(ellipse 110px 130px at 18% 45%,rgba(231,176,140,.95),transparent 75%),
    radial-gradient(ellipse 90px 150px at 6% 40%,rgba(120,76,46,.95),transparent 75%),
    radial-gradient(ellipse 14px 20px at 1% 45%,#ffffff,transparent 80%),
    radial-gradient(ellipse 200px 30px at 20% 100%,rgba(196,206,120,.8),transparent 80%),
    radial-gradient(ellipse 40px 18px at 34% 14%,rgba(255,255,255,.9),transparent 80%),
    radial-gradient(ellipse 120px 20px at 68% 55%,rgba(255,255,255,.9),transparent 80%),
    radial-gradient(ellipse 140px 30px at 80% 82%,rgba(255,255,255,.85),transparent 80%),
    linear-gradient(90deg,#cfc0a8 0%,#e4dcc9 28%,#d7e5f3 45%,#cfe0f3 100%)}
.ways-title{left:953px;top:565px;font-size:14.5px;font-weight:700;color:var(--blue);white-space:nowrap}
.ways-by{left:953px;top:587px;font-size:5.5px;color:#4a4f5a}
.ways-list{left:955px;top:622px;list-style:none;font-size:6.8px;color:#3a3f4a}
.ways-list li{display:flex;align-items:center;gap:6px;height:15px}
.tick{width:6px;height:6px;background:var(--orange);border-radius:1px;display:flex;align-items:center;justify-content:center}
.tick svg{width:5px;height:5px}

/* reviews */
.section-title{left:657px;width:650px;text-align:center;font-size:15.5px;font-weight:700;color:var(--grey-title);letter-spacing:.2px}
.video{left:657px;top:824px;width:357px;height:178px;background:#000}
.video-frame{left:708px;top:826px;width:255px;height:138px;
  background:
    radial-gradient(ellipse 70px 60px at 50% 85%,#2f4576,transparent 80%),
    radial-gradient(ellipse 26px 28px at 50% 38%,#c99077,transparent 80%),
    radial-gradient(ellipse 40px 80px at 88% 55%,#4a2e22,transparent 80%),
    radial-gradient(ellipse 22px 30px at 14% 58%,#e8e6e0,transparent 80%),
    radial-gradient(ellipse 30px 14px at 22% 12%,#6b4a34,transparent 80%),
    radial-gradient(ellipse 50px 16px at 25% 82%,#7a4d33,transparent 80%),
    linear-gradient(180deg,#d9d2c2 0%,#cbc2ad 60%,#a8977a 100%)}
.video-controls{left:657px;top:964px;width:357px;height:38px}
.quote{left:1026px;top:846px;width:201px;height:116px;background:var(--blue);border-radius:6px;color:var(--white)}
.quote p{position:absolute;left:31px;top:21px;width:156px;font-size:11px;line-height:14.6px;font-weight:400;letter-spacing:.5px}
.quote-author{left:1045px;top:972px;font-size:11px;font-style:italic;font-weight:500;color:#3a3f4a;letter-spacing:.3px}

/* help */
.help{left:657px;top:1027px;width:650px;height:278px;background:radial-gradient(ellipse at 50% 40%,#1a4270,#13335a 70%,#102d50)}
.help-title{left:657px;width:650px;top:1043px;text-align:center;font-size:15px;font-weight:700;color:var(--white)}
.tile{width:118px;height:97px;display:flex;align-items:center;justify-content:center;color:var(--white);font-size:8px;font-weight:500;letter-spacing:.5px;text-shadow:0 0 3px rgba(0,0,0,.5)}

/* news */
.news-img{width:146px;height:105px}
.news-title{width:146px;font-size:7px;font-weight:700;line-height:9.5px;color:var(--ink)}
.news-date{font-size:4.2px;color:#555;text-align:right}
.news-body{width:146px;font-size:4.4px;line-height:9.8px;color:#5a5f6a}

/* cta */
.cta{left:657px;top:1596px;width:650px;height:72px;background:var(--orange-band)}
.cta-text{left:744px;top:1617px;font-size:11px;font-weight:700;line-height:15px;color:var(--white);letter-spacing:.2px}
.field{background:var(--white);border-radius:3px;font-size:5px;color:#a0a4ad;padding:5px 8px;height:17px}
.submit{left:1161px;top:1635px;width:48px;height:17px;background:var(--navy);color:var(--white);font-size:6px;font-weight:500;border-radius:3px;display:flex;align-items:center;justify-content:center}

/* footer */
.footer{left:657px;top:1673px;width:650px;height:219px;
  background:
    radial-gradient(ellipse 260px 40px at 50% 60%,rgba(90,100,120,.35),transparent 80%),
    linear-gradient(180deg,#232935 0%,#2a3040 40%,#343b4a 62%,#1d222d 100%)}
.footer-base{left:657px;top:1892px;width:650px;height:40px;background:var(--footer-deep)}
.f-head{font-size:8px;font-weight:500;color:var(--white)}
.f-list{list-style:none;font-size:5px;color:#e6e8ee}
.f-list li{height:12.2px;display:flex;align-items:center;gap:8px}
.f-list li::before{content:"";width:0;height:0;border-left:2.5px solid #e6e8ee;border-top:2px solid transparent;border-bottom:2px solid transparent}
.f-contact{font-size:5px;color:#e6e8ee;line-height:9.5px}
.copyright{left:657px;width:650px;top:1903px;text-align:center;font-size:5px;color:#d6d9e0}
.copyright b{font-weight:400;color:var(--orange)}
</style>
</head>
<body>
<div class="stage">

  <div class="abs topbar">
    <span style="left:170px"><svg viewBox="0 0 10 10"><rect x="2.5" y=".5" width="5" height="9" rx="1" fill="none" stroke="#fff" stroke-width="1"/></svg>(555) 014-2207</span>
    <span style="left:247px"><svg viewBox="0 0 10 10"><path d="M5 .5a3.3 3.3 0 0 1 3.3 3.3C8.3 6.3 5 9.5 5 9.5S1.7 6.3 1.7 3.8A3.3 3.3 0 0 1 5 .5z" fill="#fff"/><circle cx="5" cy="3.8" r="1.2" fill="#1b4f9a"/></svg>48 Elm Row Suite 12 Farvale, NC 28990</span>
    <span style="left:403px"><svg viewBox="0 0 10 10"><circle cx="5" cy="5" r="4.2" fill="none" stroke="#fff" stroke-width="1"/><path d="M5 2.6V5l1.7 1.2" stroke="#fff" stroke-width="1" fill="none"/></svg>Mon - Fri &nbsp;8:00 - 5:00</span>
  </div>

  <div class="abs brand">
    <div class="brand-mark"></div>
    <div class="brand-name">FARVALE<br>HEARING CENTER</div>
  </div>
  <span class="abs nav active" style="left:937px">HOME</span>
  <span class="abs nav" style="left:970px">HEARING AIDS</span>
  <span class="abs nav" style="left:1027px">SERVICES</span>
  <span class="abs nav" style="left:1070px">EDUCATION</span>
  <span class="abs nav" style="left:1121px">ABOUT US</span>
  <span class="abs nav" style="left:1165px">CONTACT</span>
  <svg class="abs" style="left:1209px;top:33px" width="8" height="8" viewBox="0 0 10 10"><circle cx="4.2" cy="4.2" r="3" fill="none" stroke="#f78f20" stroke-width="1.6"/><path d="M6.4 6.4 9 9" stroke="#f78f20" stroke-width="1.6"/></svg>

  <div class="abs hero" role="img" aria-label="Photo of a smiling mother hugging her young daughter on a sofa"></div>
  <div class="abs hero-shade"></div>
  <h1 class="abs hero-title">RECAPTURE THE <em>SOUNDS OF LIFE</em></h1>
  <p class="abs hero-sub">and the intimacy of a quiet conversation</p>
  <div class="abs btn" style="left:948px;top:230px;width:81px;height:18px">TAKE ACTION TODAY</div>

  <p class="abs eyebrow">WELCOME TO</p>
  <h2 class="abs welcome-title">FARVALE HEARING CENTER LLC</h2>
  <p class="abs welcome-copy">We provide hearing evaluations, counseling, and fitting of hearing aids. We service all the major brands of hearing aids including Aurivo, Sonaris, Kellwyn, Vantel, Lumora, Brexa, Minitone, Quorix, Halden, Serell, Arcova, and others.</p>
  <div class="abs btn" style="left:744px;top:504px;width:63px;height:18px">ABOUT US</div>
  <div class="abs doctor" role="img" aria-label="Photo of the hearing specialist in a white coat with arms crossed, staff blurred behind"></div>

  <div class="abs ways" role="img" aria-label="Photo of a laughing girl with a daisy in her hair against a bright sky"></div>
  <h2 class="abs ways-title">50 WAYS TO CHERISH YOUR HEARING</h2>
  <p class="abs ways-by">by Warren Pell</p>
  <ul class="abs ways-list">
    <li><span class="tick"><svg viewBox="0 0 10 10"><path d="M2 5.2 4.2 7.4 8 3" stroke="#fff" stroke-width="1.6" fill="none"/></svg></span>Bi-Annual Hearing Checkups</li>
    <li><span class="tick"><svg viewBox="0 0 10 10"><path d="M2 5.2 4.2 7.4 8 3" stroke="#fff" stroke-width="1.6" fill="none"/></svg></span>20 db Hearing or Better</li>
    <li><span class="tick"><svg viewBox="0 0 10 10"><path d="M2 5.2 4.2 7.4 8 3" stroke="#fff" stroke-width="1.6" fill="none"/></svg></span>Quiet Conversation</li>
    <li><span class="tick"><svg viewBox="0 0 10 10"><path d="M2 5.2 4.2 7.4 8 3" stroke="#fff" stroke-width="1.6" fill="none"/></svg></span>Music</li>
    <li><span class="tick"><svg viewBox="0 0 10 10"><path d="M2 5.2 4.2 7.4 8 3" stroke="#fff" stroke-width="1.6" fill="none"/></svg></span>Dancing</li>
  </ul>
  <div class="abs btn" style="left:955px;top:723px;width:63px;height:18px">READ MORE</div>

  <h2 class="abs section-title" style="top:795px">OUR PATIENTS REVIEWS</h2>
  <div class="abs video"></div>
  <div class="abs video-frame" role="img" aria-label="Video still of a patient seated in the clinic office giving a testimonial"></div>
  <svg class="abs" style="left:808px;top:886px" width="54" height="54" viewBox="0 0 54 54"><circle cx="27" cy="27" r="26" fill="rgba(255,255,255,.85)"/><path d="M21 15 40 27 21 39z" fill="#1a1a1a"/></svg>
  <svg class="abs video-controls" viewBox="0 0 357 38">
    <rect x="2" y="3" width="350" height="2" fill="#555"/>
    <rect x="2" y="3" width="340" height="2" fill="#e02020"/>
    <path d="M17 15 29 22 17 29z" fill="#fff"/>
    <path d="M50 16 57 22 50 28zM57 16 64 22 57 28z" fill="#fff"/><rect x="64" y="16" width="2" height="12" fill="#fff"/>
    <path d="M83 19h4l5-4v14l-5-4h-4z" fill="#fff"/><path d="M94 18c2 2 2 6 0 8" stroke="#fff" stroke-width="1.5" fill="none"/>
    <rect x="105" y="21" width="19" height="2" fill="#e02020"/>
    <text x="131" y="26" font-family="Poppins,sans-serif" font-size="9" fill="#fff">1:34 / 1:38</text>
    <rect x="234" y="17" width="14" height="10" rx="1.5" fill="none" stroke="#fff" stroke-width="1.5"/><text x="236.5" y="25" font-family="Poppins,sans-serif" font-size="6" font-weight="700" fill="#fff">CC</text>
    <circle cx="273" cy="22" r="6" fill="none" stroke="#fff" stroke-width="3" stroke-dasharray="3 2"/><circle cx="273" cy="22" r="2" fill="#fff"/>
    <rect x="275" y="11" width="9" height="6" rx="1" fill="#e02020"/>
    <rect x="298" y="18" width="12" height="8" fill="none" stroke="#fff" stroke-width="2"/>
    <path d="M327 20v-4h4M339 16h4v4M343 25v4h-4M331 29h-4v-4" stroke="#fff" stroke-width="2" fill="none"/>
  </svg>
  <div class="abs quote">
    <svg class="abs" style="left:9px;top:9px" width="18" height="10" viewBox="0 0 18 10"><circle cx="4" cy="4" r="3.5" fill="#fff"/><path d="M1 5 3 10 6 6z" fill="#fff"/><circle cx="13" cy="4" r="3.5" fill="#fff"/><path d="M10 5 12 10 15 6z" fill="#fff"/></svg>
    <p>If you need hearing aids or have a hearing problem, come see Warren Pell.</p>
    <svg class="abs" style="left:118px;top:115px" width="12" height="7" viewBox="0 0 12 7"><path d="M0 0h12L6 7z" fill="#0255a3"/></svg>
  </div>
  <p class="abs quote-author">Dale Hartwick</p>

  <div class="abs help"></div>
  <h2 class="abs help-title">HOW CAN WE HELP YOU?</h2>
  <div class="abs tile" style="left:798px;top:1079px;background:radial-gradient(ellipse 40px 50px at 45% 35%,#d8a083,transparent 80%),radial-gradient(ellipse 50px 60px at 85% 80%,#4a3a36,transparent 80%),linear-gradient(135deg,#8f7462,#b58a70 50%,#6d574e)" role="img" aria-label="Close-up photo of an ear">Hearing Aids</div>
  <div class="abs tile" style="left:924px;top:1079px;background:radial-gradient(ellipse 40px 40px at 45% 25%,#fff3b0,transparent 80%),radial-gradient(ellipse 40px 50px at 80% 70%,#e8b8a6,transparent 80%),linear-gradient(170deg,#f4b434,#e88a22 55%,#c66a22)" role="img" aria-label="Photo of a woman outdoors at sunset">Tinnitus Treatment</div>
  <div class="abs tile" style="left:1047px;top:1079px;background:radial-gradient(ellipse 50px 20px at 50% 45%,#c8dde6,transparent 80%),radial-gradient(ellipse 30px 20px at 40% 80%,#d9a58e,transparent 80%),linear-gradient(135deg,#5d9ab8,#3f7d9f 55%,#7fb0c6)" role="img" aria-label="Photo of a man swimming in a pool">Ear Molds (Protection)</div>
  <div class="abs tile" style="left:798px;top:1182px;background:radial-gradient(ellipse 30px 40px at 30% 40%,#e3dcd3,transparent 80%),radial-gradient(ellipse 40px 50px at 75% 45%,#d3b08f,transparent 80%),linear-gradient(135deg,#8c8a7c,#b7a98d 55%,#6f6a5c)" role="img" aria-label="Photo of a smiling senior couple">F.A.Q.</div>
  <div class="abs tile" style="left:924px;top:1182px;background:radial-gradient(ellipse 30px 40px at 30% 45%,#c9c7c4,transparent 80%),radial-gradient(ellipse 40px 50px at 70% 40%,#6b4f43,transparent 80%),radial-gradient(ellipse 60px 30px at 40% 90%,#4c5e80,transparent 80%),linear-gradient(135deg,#9c958d,#5f5a5a 55%,#b9b1a7)" role="img" aria-label="Photo of an older man and his son reading together">Tips for Wearers</div>
  <div class="abs tile" style="left:1047px;top:1182px;background:radial-gradient(ellipse 30px 30px at 55% 25%,#c99077,transparent 80%),radial-gradient(ellipse 60px 50px at 55% 85%,#9a7b55,transparent 80%),linear-gradient(180deg,#2e2f36,#5a5048 45%,#8a7256)" role="img" aria-label="Photo of a man on the phone by a city window">Schedule an Appointment</div>

  <h2 class="abs section-title" style="top:1330px">LATEST NEWS</h2>

  <div class="abs news-img" style="left:744px;top:1369px;background:radial-gradient(ellipse 40px 50px at 55% 55%,#d9ab92,transparent 80%),radial-gradient(ellipse 40px 60px at 85% 30%,#4a3328,transparent 80%),radial-gradient(ellipse 20px 30px at 30% 30%,#c99a84,transparent 80%),linear-gradient(135deg,#e2ddd8,#cfc7c0 55%,#b9aba0)" role="img" aria-label="Photo of a woman cupping her ear to listen"></div>
  <h3 class="abs news-title" style="left:745px;top:1479px">Do's and Don'ts for Communicating During the Holidays</h3>
  <p class="abs news-date" style="left:845px;top:1491px;width:42px">12/19/2018</p>
  <p class="abs news-body" style="left:745px;top:1505px">It's important to make sure that everyone is comfortable and getting what they need in large group settings, and using these tips for talking with people who have hearing loss may help everyone feel more included. If you think it might help, be sure to pass this along to your family and friends just in time for the next holiday party.</p>

  <div class="abs news-img" style="left:908px;top:1369px;background:radial-gradient(ellipse 40px 40px at 35% 25%,#f3f1ee,transparent 80%),radial-gradient(ellipse 40px 50px at 40% 60%,#e0b39e,transparent 80%),radial-gradient(ellipse 40px 40px at 40% 95%,#4fa6b5,transparent 80%),linear-gradient(90deg,#e7e3dd,#cdc6bd 55%,#6fa6d0)" role="img" aria-label="Photo of a senior woman adjusting her hearing aid"></div>
  <h3 class="abs news-title" style="left:909px;top:1479px">Communication for All: How People of All Ages Benefit from Better Hearing and Communication</h3>
  <p class="abs news-date" style="left:1012px;top:1500px;width:42px">5.01.2018</p>
  <p class="abs news-body" style="left:909px;top:1514px">Regardless of age, occupation or gender everyone can benefit from clear communication and healthy hearing. Check out this article, crafted to celebrate Better Hearing and Speech Month.</p>

  <div class="abs news-img" style="left:1073px;top:1369px;background:radial-gradient(ellipse 30px 50px at 25% 55%,#f6f6f6,transparent 80%),radial-gradient(ellipse 20px 20px at 22% 40%,#8a5b3e,transparent 80%),radial-gradient(ellipse 30px 30px at 75% 40%,#d7d0ca,transparent 80%),radial-gradient(ellipse 40px 20px at 60% 85%,#bdb8b2,transparent 80%),linear-gradient(135deg,#fbfbfb,#eeeeee 55%,#d9d6d2)" role="img" aria-label="Photo of an audiologist testing a patient's hearing in a booth"></div>
  <h3 class="abs news-title" style="left:1074px;top:1479px">Over-the-Counter Hearing Aids: What You Need to Know</h3>
  <p class="abs news-date" style="left:1176px;top:1491px;width:42px">9.14.2017</p>
  <p class="abs news-body" style="left:1074px;top:1505px">In August 2017, a law was passed that allows FDA-regulated hearing aids to be sold over the counter instead of by a trained hearing healthcare professional.</p>

  <div class="abs cta"></div>
  <p class="abs cta-text">TAKE ACTION! MAKE AN APPOINTMENT<br>FOR A HEARING EVALUATION.</p>
  <div class="abs field" style="left:998px;top:1611px;width:101px">Name</div>
  <div class="abs field" style="left:1108px;top:1611px;width:101px">Email</div>
  <div class="abs field" style="left:998px;top:1635px;width:158px">Message</div>
  <div class="abs submit">SUBMIT</div>

  <div class="abs footer" role="img" aria-label="Dim photo of a city skyline at dusk behind the footer links"></div>
  <p class="abs f-head" style="left:744px;top:1724px">Home</p>
  <ul class="abs f-list" style="left:744px;top:1749px"><li>Welcome</li><li>Healthcare News</li></ul>
  <p class="abs f-head" style="left:744px;top:1782px">Hearing Aids</p>
  <ul class="abs f-list" style="left:744px;top:1798px"><li>Brands</li><li>Repairs/Maintenance</li><li>Batteries</li><li>Featured Technology</li></ul>

  <p class="abs f-head" style="left:869px;top:1724px">Services</p>
  <ul class="abs f-list" style="left:869px;top:1749px"><li>Tinnitus Treatment</li><li>Insurance Financing</li></ul>
  <p class="abs f-head" style="left:869px;top:1782px">Education</p>
  <ul class="abs f-list" style="left:869px;top:1798px"><li>Frequently asked question</li><li>Hearing Myths</li><li>Tips for hearing aid</li><li>Members</li></ul>

  <p class="abs f-head" style="left:1000px;top:1724px">About Us</p>
  <ul class="abs f-list" style="left:1000px;top:1749px"><li>Meet the specialist</li><li>Video testimonials</li></ul>
  <p class="abs f-head" style="left:1000px;top:1782px">Contact</p>
  <ul class="abs f-list" style="left:1000px;top:1798px"><li>Location &amp; Map</li><li>new patient form</li><li>Links</li></ul>

  <p class="abs f-head" style="left:1132px;top:1723px;font-weight:300;font-size:9px">Contact us</p>
  <svg class="abs" style="left:1130px;top:1749px" width="6" height="7" viewBox="0 0 10 12"><path d="M5 .5a4 4 0 0 1 4 4C9 7.5 5 11.5 5 11.5S1 7.5 1 4.5a4 4 0 0 1 4-4z" fill="#fff"/><circle cx="5" cy="4.5" r="1.4" fill="#2a3142"/></svg>
  <p class="abs f-contact" style="left:1146px;top:1748px">48 Elm Row Suite 12<br>Farvale, NC 28990<br><span style="text-decoration:underline">Send us email</span></p>
  <svg class="abs" style="left:1130px;top:1770px" width="7" height="5" viewBox="0 0 14 10"><rect width="14" height="10" rx="1" fill="#fff"/><path d="M0 1 7 6 14 1" stroke="#2a3142" stroke-width="1.3" fill="none"/></svg>
  <svg class="abs" style="left:1131px;top:1788px" width="5" height="8" viewBox="0 0 6 10"><rect x=".5" y=".5" width="5" height="9" rx="1" fill="none" stroke="#fff"/></svg>
  <p class="abs f-contact" style="left:1147px;top:1787px">(555) 014-2207</p>

  <div class="abs footer-base"></div>
  <p class="abs copyright">Copyright @ 2019 <b>Farvale Hearing Center LLC Healthcare</b></p>

</div>
</body>
</html>
```